Vardena General Painting Ltd. - Construction painting company providing high-quality service

We need a logo and business card design for a painting company that provides high-quality work for major developers and builders in Calgary, Alberta. Our projects include commercial high-rise residential towers. We would like designs that communicate professionalism and high quality service.
Updates
Need extra days to review
Target Market(s)
Developers and builders
Industry/Entity Type
Construction
Contact Information for Business Card
Company name, employee name, title, phone number, email address
Font styles to use
Colors
Designer to choose colors to be used in the design.
Look and feel
Each slider illustrates characteristics of the customer's brand and the style your logo design should communicate.

```html
<!DOCTYPE html>
<html lang="en">
<head>
<meta charset="utf-8">
<title>Vardena General Painting – Business Card</title>
<link rel="stylesheet" href="https://fonts.googleapis.com/css2?family=Montserrat:wght@400;700;800&display=swap">
<style>
  :root {
    --stage: #000000;
    --card: #ffffff;
    --ink: #0b0b0b;
    --accent: #0b74bf;
  }
  * { margin: 0; padding: 0; box-sizing: border-box; }
  html, body { width: 1200px; height: 1000px; overflow: hidden; background: var(--stage); }
  body { position: relative; font-family: "Montserrat", Arial, sans-serif; color: var(--ink); }

  .card {
    position: absolute;
    left: 338px;
    width: 524px;
    height: 299px;
    background: var(--card);
    overflow: hidden;
  }
  .card--front { top: 160px; }
  .card--back { top: 505px; }

  .accent-band {
    position: absolute;
    left: 0; right: 0; bottom: 0;
    height: 11px;
    background: var(--accent);
  }

  .brand {
    position: absolute;
    display: flex;
    flex-direction: column;
    align-items: center;
    color: var(--ink);
  }
  .brand-dot {
    border-radius: 50%;
    background: var(--accent);
  }
  .brand-name { font-weight: 800; font-size: 40px; line-height: 1; letter-spacing: 0.3px; }
  .brand-tag { font-weight: 400; font-size: 16.5px; line-height: 1; letter-spacing: 1.5px; margin-top: 7px; }

  .card--front .brand { left: 0; right: 0; top: 50px; }
  .card--front .brand-dot { width: 104px; height: 104px; margin-bottom: 28px; }

  .card--back .brand { left: 30px; width: 220px; top: 50px; }
  .card--back .brand-dot { width: 104px; height: 104px; margin-bottom: 28px; }

  .divider {
    position: absolute;
    left: 278px;
    top: 51px;
    width: 2px;
    height: 190px;
    background: var(--ink);
  }

  .person { position: absolute; left: 313px; top: 66px; }
  .person-name { font-weight: 700; font-size: 20px; letter-spacing: 0.8px; line-height: 1.1; }
  .person-title { font-weight: 400; font-size: 15px; letter-spacing: 0.8px; margin-top: 3px; }

  .contact {
    position: absolute;
    left: 314px;
    top: 181px;
    list-style: none;
    font-size: 15px;
    line-height: 21px;
    font-weight: 400;
  }
</style>
</head>
<body>

  <section class="card card--front" aria-label="Business card front">
    <div class="brand">
      <div class="brand-dot"></div>
      <div class="brand-name">VARDENA</div>
      <div class="brand-tag">GENERAL PAINTING</div>
    </div>
    <div class="accent-band"></div>
  </section>

  <section class="card card--back" aria-label="Business card back">
    <div class="brand">
      <div class="brand-dot"></div>
      <div class="brand-name">VARDENA</div>
      <div class="brand-tag">GENERAL PAINTING</div>
    </div>
    <div class="divider"></div>
    <div class="person">
      <div class="person-name">MARK DELANEY</div>
      <div class="person-title">PRESIDENT</div>
    </div>
    <ul class="contact">
      <li>(403) 555-0148</li>
      <li>mark@vardena.com</li>
      <li>www.vardena.com</li>
    </ul>
    <div class="accent-band"></div>
  </section>

</body>
</html>
```